8x8 Social Media Ad - Summit Harbor Expo

Attention Real Estate Agents
Please join us for our
Quarterly Real Estate Training Expo
The 2nd Saturday of February, May, August and November
Our Next Training Expo is _________________________________
From 9 am to 1 pm
at
Marlowe Suites Fernfield Oak Ridge
4187 Copper Meadow Lane, Fernfield, MD 20994
Scheduled Speakers
9:00 am - Malcolm Prewitt - Orientation
9:30 am - Darnell Ockley - Multiple Income Streams / Pivot Program
10:00 am - Keira Lindqvist - Marketing though Social Media
10:45 am - Owen Trask - Generating Business through Lumo-Net
11:30 am - Ada Nwachime - Real Estate Investing
12:15 pm - Gregory Tamsin - (Main Speaker) Training Topic TBA
For more information call Malcolm Prewitt at (240) 555-0182 or email mprewitt@summitharborhomes.example

```html
<!DOCTYPE html>
<html lang="en">
<head>
<meta charset="utf-8">
<title>Summit Harbor Expo – Quarterly Real Estate Training Expo</title>
<link href="https://fonts.googleapis.com/css2?family=Montserrat:wght@300;400;500;600;700;800;900&display=swap" rel="stylesheet">
<style>
  :root{
    --teal:#0a8299;
    --teal-deep:#08727a;
    --teal-light:#0b8ea6;
    --red:#d91f26;
    --paper:#f7f9f9;
    --mist:#dfe7e7;
    --mist-dark:#c9d5d5;
  }
  *{margin:0;padding:0;box-sizing:border-box}
  html,body{width:1200px;height:1200px;overflow:hidden;background:var(--paper)}
  body{font-family:"Montserrat",sans-serif;color:var(--teal)}
  .ad{position:relative;width:1200px;height:1200px;overflow:hidden;background:var(--paper)}
  .abs{position:absolute}

  .skyline{left:0;top:780px;width:1200px;height:420px;
    background:linear-gradient(180deg,rgba(223,231,231,0) 0%,var(--mist) 55%,var(--mist-dark) 100%)}

  .brand{left:22px;top:46px;display:flex;align-items:center;gap:8px;
    font-weight:800;font-size:25px;color:var(--teal);line-height:1;white-space:nowrap}
  .brand-square{width:22px;height:22px;background:var(--teal)}

  .attention{left:284px;width:606px;top:24px;text-align:center;font-size:41px;font-weight:500;color:var(--teal-deep);white-space:nowrap}
  .quarterly{left:413px;top:85px;width:373px;height:69px;background:var(--teal);color:#fff;
    font-weight:800;font-size:49px;display:flex;align-items:center;justify-content:center;letter-spacing:1px}

  .headline{left:0;top:160px;width:1200px;height:220px;overflow:visible}
  .headline text{font-family:"Montserrat",sans-serif;font-weight:900}

  .join{left:489px;top:391px;width:221px;height:71px;background:var(--red);border-radius:8px;color:#fff;
    font-weight:900;font-size:40px;display:flex;align-items:center;justify-content:center}

  .speaker{position:absolute;width:159px}
  .photo{width:159px;height:151px;border-radius:38px 38px 0 38px;
    background:linear-gradient(180deg,var(--teal) 0%,#2c6f78 55%,#3b3b3b 100%)}
  .speaker-name{margin-top:12px;text-align:right;font-weight:600;font-size:17px;white-space:nowrap;color:var(--teal)}
  .speaker-topic{text-align:right;font-weight:300;font-size:13.5px;line-height:1.12;color:var(--teal);margin-top:4px;white-space:nowrap}

  .divider-v{left:719px;top:494px;width:2px;height:487px;background:var(--teal)}
  .next{left:760px;width:392px;top:470px;text-align:center;font-weight:800;font-size:50px;line-height:1.24;color:var(--teal)}
  .divider-h{left:784px;top:729px;width:342px;height:2px;background:var(--teal)}

  .day{left:774px;top:780px;font-weight:800;font-size:98px;line-height:1;color:var(--teal);letter-spacing:-3px}
  .month{left:916px;top:800px;font-weight:700;font-size:30px;line-height:1.15;color:var(--teal)}
  .time{left:774px;top:877px;width:361px;height:39px;border-radius:10px;background:var(--teal);color:#fff;
    font-weight:700;font-size:30px;display:flex;align-items:center;justify-content:center}

  .pin{left:895px;top:940px}
  .venue-frame{left:663px;top:1028px;width:514px;height:88px;border:1.5px dashed var(--teal);border-radius:14px}
  .venue-tag{left:871px;top:1013px;width:98px;height:30px;border:1.5px solid var(--teal);border-radius:7px;background:var(--paper);
    font-weight:700;font-size:17px;display:flex;align-items:center;justify-content:center;color:var(--teal-deep)}
  .venue-text{left:663px;top:1054px;width:514px;text-align:center;font-weight:500;font-size:17px;line-height:1.3;color:var(--teal);white-space:nowrap}

  .scheduled{left:140px;top:1031px;width:446px;height:53px;border-radius:14px;
    background:linear-gradient(180deg,var(--teal) 0%,var(--teal-deep) 100%);
    color:#e9f2f3;font-weight:800;font-size:33px;display:flex;align-items:center;justify-content:center;letter-spacing:.5px}

  .footer-rule{left:0;top:1157px;width:1200px;height:3px;background:var(--teal)}
  .footer{left:76px;top:1143px;width:1041px;height:31px;border-radius:9px;background:var(--teal);color:#fff;
    font-weight:600;font-size:15.5px;display:flex;align-items:center;justify-content:center;white-space:nowrap;overflow:hidden}
  .footer-band{left:0;top:1180px;width:1200px;height:20px;background:var(--mist-dark)}
</style>
</head>
<body>
<main class="ad">
  <div class="abs skyline" role="img" aria-label="Faint city skyline illustration behind the lower half"></div>

  <div class="abs brand"><span class="brand-square"></span>Summit Harbor</div>

  <p class="abs attention">Attention Real Estate Agents</p>
  <div class="abs quarterly">QUARTERLY</div>

  <svg class="abs" style="left:1006px;top:152px" width="74" height="62" viewBox="0 0 74 62">
    <path d="M0 2 L71 0 L68 60" fill="none" stroke="var(--teal)" stroke-width="4"/>
  </svg>
  <svg class="abs" style="left:160px;top:334px" width="70" height="62" viewBox="0 0 70 62">
    <path d="M3 0 L2 59 L70 58" fill="none" stroke="var(--teal)" stroke-width="4"/>
  </svg>

  <svg class="abs headline" viewBox="0 0 1200 220" role="heading" aria-level="1" aria-label="Real Estate Training Expo">
    <defs>
      <linearGradient id="split-one" gradientUnits="userSpaceOnUse" x1="0" y1="20" x2="0" y2="110">
        <stop offset="0.5" stop-color="#0b8ea6"/><stop offset="0.5" stop-color="#08727a"/>
      </linearGradient>
      <linearGradient id="split-two" gradientUnits="userSpaceOnUse" x1="0" y1="131" x2="0" y2="206">
        <stop offset="0.5" stop-color="#0b8ea6"/><stop offset="0.5" stop-color="#08727a"/>
      </linearGradient>
    </defs>
    <text x="181" y="110" font-size="128" textLength="867" lengthAdjust="spacingAndGlyphs" fill="url(#split-one)">REAL ESTATE</text>
    <text x="181" y="206" font-size="107" textLength="867" lengthAdjust="spacingAndGlyphs" fill="url(#split-two)">TRAINING EXPO</text>
  </svg>

  <div class="abs join">JOIN US</div>

  <section class="speakers">
    <div class="speaker" style="left:47px;top:517px">
      <div class="photo" role="img" aria-label="Portrait of Malcolm Prewitt"></div>
      <p class="speaker-name">MALCOLM PREWITT</p>
      <p class="speaker-topic">Orientation</p>
    </div>
    <div class="speaker" style="left:294px;top:517px">
      <div class="photo" role="img" aria-label="Portrait of Darnell Ockley"></div>
      <p class="speaker-name">DARNELL OCKLEY</p>
      <p class="speaker-topic">Multiple Income Streams<br>/ Pivot Program</p>
    </div>
    <div class="speaker" style="left:520px;top:517px">
      <div class="photo" role="img" aria-label="Portrait of Keira Lindqvist"></div>
      <p class="speaker-name">KEIRA LINDQVIST</p>
      <p class="speaker-topic">Marketing through<br>Social Media</p>
    </div>
    <div class="speaker" style="left:47px;top:782px">
      <div class="photo" role="img" aria-label="Portrait of Owen Trask"></div>
      <p class="speaker-name">OWEN TRASK</p>
      <p class="speaker-topic">Generating Business<br>through Lumo-Net</p>
    </div>
    <div class="speaker" style="left:284px;top:782px">
      <div class="photo" role="img" aria-label="Portrait of Ada Nwachime"></div>
      <p class="speaker-name">ADA NWACHIME</p>
      <p class="speaker-topic">Real Estate Investing</p>
    </div>
    <div class="speaker" style="left:520px;top:782px">
      <div class="photo" role="img" aria-label="Portrait of Gregory Tamsin"></div>
      <p class="speaker-name">GREGORY TAMSIN</p>
      <p class="speaker-topic"><span style="font-weight:400">(Main Speaker)</span><br>Training Topic TBA</p>
    </div>
  </section>

  <div class="abs divider-v"></div>

  <p class="abs next">OUR NEXT<br>TRAINING<br>EXPO</p>
  <div class="abs divider-h"></div>

  <p class="abs day">02</p>
  <p class="abs month">AUGUST, 2023<br>SATURDAY</p>
  <div class="abs time">9 AM TO 1 PM</div>

  <svg class="abs pin" width="50" height="74" viewBox="0 0 50 74" aria-hidden="true">
    <path d="M25 2 C11 2 2 12 2 25 C2 42 25 72 25 72 C25 72 48 42 48 25 C48 12 39 2 25 2 Z" fill="var(--red)"/>
    <circle cx="25" cy="24" r="9" fill="#fff"/>
  </svg>

  <div class="abs venue-frame"></div>
  <div class="abs venue-tag">VENUE</div>
  <p class="abs venue-text">MARLOWE SUITES FERNFIELD OAK RIDGE<br>4187 COPPER MEADOW LANE, FERNFIELD, MD 20994</p>

  <div class="abs scheduled">SCHEDULED SPEAKERS</div>

  <div class="abs footer-rule"></div>
  <p class="abs footer">For more information call Malcolm Prewitt at (240) 555-0182 or email - mprewitt@summitharborhomes.example</p>
  <div class="abs footer-band"></div>
</main>
</body>
</html>
```